Additional page needed for existing website

I have an existing website www.kelpsentry.co.uk and I need two additional page adding to the website. We offer a service that allows a parent to understand what their children are doing online and block inappropriate content, its a "parental control" app. It currently only works with Vemra devices.
The features of the service are -
Block inappropriate content, we block over 100 million websites.
Set Device Access Times, you can set times that the device can access the Internet.
App Management, Kelp Sentry will scan the device every hour and detect any risky apps that have been installed.
Dashboard shows what websites have been visited.

First page -
The new page will have a page name of "Korvo Parental Control App"
The meta title tag is "Korvo 6 Parental Control App | VEMRA Parental Control App | Kelp Sentry" and Meta Description Tag of "“If your child has an Korvo and you want to check which apps they mostly use then Install Kelp Sentry Parental Control App for Korvo, Tabrix, and VEMRA. Download Here."
We need content on the page of around 300-500 words. (keyword density should not be more than 2%)
Keywords are
· orvane korvo parental controls
· korvo 6 parental controls
· vemra parental control app
· vemra parental controls
· korvo parental controls
· best parental control app for Korvo

The type of thing we are after is similar to
https://dalvoreach.io/features/vemra.html
https://www.trenlox.com/parental-control.html

Second new page -
Page name - Tabrix Parental Control App
Meta Tag Title - Tabrix Parental Control App | Kelp Sentry
Meta Description Tag -
"Being a parent your biggest concern is what content your child will see on their Tabrix. You can do it easily now with the help of Kelp Sentry Parental Control App for Korvo, Tabrix, and VEMRA. Download Now. "

Keywords -
· best parental control app for tabrix
· parental control app for tabrix
· parental restrictions on tabrix

Similar to this
https://www.pashtree.com/parental-controls/vemra-tabrix

```html
<!DOCTYPE html>
<html lang="en">
<head>
<meta charset="utf-8">
<title>Korvo Parental Control App | Kelp Sentry</title>
<link href="https://fonts.googleapis.com/css2?family=Open+Sans:wght@400;600;700&family=Roboto+Slab:wght@600;700&display=swap" rel="stylesheet">
<style>
:root{
  --blue:#3289d0;
  --blue-dark:#1d4f7c;
  --nav-blue:#3e8cc8;
  --orange:#f5a623;
  --ink:#1f2326;
  --grey:#8a8f94;
  --line:#e3e6e9;
  --band:#e7f1f9;
  --white:#fff;
}
*{box-sizing:border-box;margin:0;padding:0}
html,body{width:1200px;height:4054px;overflow:hidden;background:var(--white)}
body{position:relative;font-family:"Open Sans",sans-serif;color:var(--ink)}
.abs{position:absolute}
a{text-decoration:none;color:inherit}
.link{color:var(--blue);font-size:13px;font-weight:600}
.eyebrow{color:var(--blue);font-size:13px}
.h2{font-weight:600;font-size:27px;line-height:34px;color:var(--ink)}
.muted{color:var(--grey);font-size:12.5px;line-height:26px}

/* hero */
.hero{left:0;top:0;width:1200px;height:553px;background:linear-gradient(100deg,#3d6f93 0%,#6e9bb8 45%,#a9c4d3 75%,#cdd9de 100%)}
.nav{left:230px;top:0;width:735px;height:69px;display:flex}
.nav-brand{width:128px;background:var(--white);display:flex;align-items:center;justify-content:center;gap:6px;font-weight:700;font-size:15px;color:var(--blue-dark)}
.nav-brand i{width:14px;height:14px;border-radius:50%;background:var(--blue)}
.nav-links{flex:1;background:rgba(62,140,200,.55);display:flex;align-items:center;gap:13px;padding-left:22px;font-family:"Roboto Slab",serif;font-weight:700;font-size:11.5px;color:var(--white)}
.nav-links .active{border-bottom:2px solid var(--white);padding-bottom:3px}
.nav-links .hl{color:var(--orange)}
.nav-login{width:72px;background:var(--blue-dark);color:var(--white);display:flex;align-items:center;justify-content:center;font-family:"Roboto Slab",serif;font-weight:700;font-size:12px}
.hero-title{left:120px;top:200px;font-size:42px;font-weight:700;color:var(--white)}
.hero-sub{left:120px;top:258px;font-size:23px;font-weight:600;color:var(--white)}
.hero-copy{left:120px;top:314px;width:470px;font-size:12px;line-height:22px;color:#eef4f8}
.btn{top:387px;height:33px;border-radius:17px;font-size:10px;display:flex;align-items:center;justify-content:center;gap:8px;text-transform:uppercase}
.btn-dark{left:120px;width:145px;background:#15191c;color:var(--white)}
.btn-dark i{width:9px;height:9px;border-radius:50%;background:var(--white)}
.btn-ghost{left:274px;width:110px;border:1.5px solid rgba(255,255,255,.8);color:var(--white)}
.phone{background:#111;border-radius:28px;padding:9px}
.phone .screen{width:100%;height:100%;background:var(--white);border-radius:20px;display:flex;align-items:center;justify-content:center;font-weight:700;font-size:15px;color:var(--blue-dark)}

/* intro */
.feature-box{left:609px;top:658px;width:421px;height:311px;border:1px solid var(--line)}
.fb-item{position:absolute;left:0;width:100%;padding:0 28px 0 86px}
.fb-item h4{font-size:13px;font-weight:600;margin-bottom:4px}
.fb-item p{font-size:11px;line-height:14px;color:var(--grey)}
.fb-item svg{position:absolute;left:48px;top:0}
.fb-sep{position:absolute;left:0;width:100%;height:1px;background:var(--line)}

/* dashboard */
.band{left:0;top:1670px;width:1200px;height:483px;background:var(--band)}
.app{background:var(--white);border-radius:14px;box-shadow:0 4px 14px rgba(0,0,0,.08);font-size:9.5px}
.app-row{display:flex;align-items:center;gap:12px;height:34px}
.app-row b{width:20px;height:20px;border-radius:4px;display:block}
.app-row span{flex:1;border-bottom:1px solid #ccc;padding-bottom:3px}

/* grid */
.cell{position:absolute;width:310px;text-align:center}
.cell h4{font-size:13px;font-weight:600;margin:12px 0 8px}
.cell p{font-size:11px;line-height:15px;color:var(--grey);padding:0 30px}

/* reviews */
.card{top:3457px;width:243px;height:295px;border:1.5px solid var(--line);border-radius:10px;padding:34px 22px 0}
.card p{font-size:11.5px;line-height:21px;color:var(--grey)}
.author{position:absolute;left:38px;top:219px;display:flex;align-items:center;gap:14px}
.author i{width:38px;height:38px;border-radius:50%;background:#c9a58e;display:block}
.author b{font-weight:400;font-size:12.5px;display:block}
.author small{font-size:9px;color:var(--grey)}

.footer-links{left:0;top:3945px;width:1200px;display:flex;justify-content:center;gap:15px;font-family:"Roboto Slab",serif;font-weight:700;font-size:11.5px}
.copy{left:0;top:4003px;width:1200px;text-align:center;font-family:"Roboto Slab",serif;font-size:11.5px}
</style>
</head>
<body>

<header class="abs hero" role="img" aria-label="Photo of a mother and daughter looking at a phone together"></header>
<nav class="abs nav">
  <div class="nav-brand"><i></i>Kelp Sentry</div>
  <div class="nav-links">
    <a class="active">HOME</a><a>ABOUT ▾</a><a>HELP</a><a class="hl">PLANS AND PRICING</a><a>OUR TEAM</a><a>BLOG</a><a>CONTACT US</a>
  </div>
  <a class="nav-login">LOGIN</a>
</nav>
<h1 class="abs hero-title">Keep Your Children SAFE!</h1>
<p class="abs hero-sub">The #1 Parental Control App for Korvo</p>
<p class="abs hero-copy">If your child has an Korvo and you want to check which apps they mostly use then Install Kelp Sentry Parental Control App for Korvo, Tabrix, and Vemra.</p>
<a class="abs btn btn-dark"><i></i>Download now</a>
<a class="abs btn btn-ghost">Learn more</a>
<div class="abs phone" style="left:879px;top:154px;width:201px;height:422px"><div class="screen">Kelp Sentry</div></div>
<div class="abs phone" style="left:800px;top:244px;width:164px;height:343px;border:3px solid #ddd"><div class="screen">Kelp Sentry</div></div>

<!-- intro -->
<p class="abs eyebrow" style="left:150px;top:681px">Best parental control app for Vemra</p>
<h2 class="abs h2" style="left:150px;top:704px">It’s far more than an ordinary<br>parental control app.</h2>
<p class="abs muted" style="left:150px;top:788px;width:360px">Kelp Sentry is the best parental control app ever made with super easy ways to monitor, manage and limit your kids’ device usage.</p>
<a class="abs link" style="left:150px;top:882px">Learn more →</a>

<div class="abs feature-box">
  <div class="fb-item" style="top:34px">
    <svg width="22" height="22" viewBox="0 0 22 22"><circle cx="11" cy="11" r="9" fill="none" stroke="#1d4f7c" stroke-width="2"/><path d="M5 5l12 12" stroke="#1d4f7c" stroke-width="2"/></svg>
    <h4>Blocking Inappropriate Content</h4>
    <p>We allow a parent to understand what their children are doing online and block inappropriate content. Currently we’re blocking over 100 million websites.</p>
  </div>
  <div class="fb-sep" style="top:116px"></div>
  <div class="fb-item" style="top:135px">
    <svg width="20" height="20" viewBox="0 0 20 20" fill="none" stroke="#1d4f7c" stroke-width="1.8"><rect x="1" y="1" width="7" height="7"/><rect x="12" y="1" width="7" height="7"/><rect x="1" y="12" width="7" height="7"/><rect x="12" y="12" width="7" height="7"/></svg>
    <h4>App Management</h4>
    <p>Kelp Sentry will scan the device every hour and detect any risky apps that have been installed.</p>
  </div>
  <div class="fb-sep" style="top:218px"></div>
  <div class="fb-item" style="top:236px">
    <svg width="22" height="22" viewBox="0 0 22 22" fill="none" stroke="#1d4f7c" stroke-width="2"><path d="M11 2a9 9 0 1 1-8 5"/><path d="M11 6v5l3 2"/></svg>
    <h4>Set Device Access Times</h4>
    <p>You can set times that the device can access the Internet.</p>
  </div>
</div>

<!-- divider -->
<svg class="abs" style="left:0;top:1015px" width="1200" height="80" viewBox="0 0 1200 80" fill="none" stroke="#3289d0" stroke-width="1">
  <path d="M0 13H254M266 17L285 40H562M636 40H937L958 64H1200"/>
  <circle cx="260" cy="13" r="5" fill="#fff"/><circle cx="963" cy="70" r="5" fill="#fff"/>
  <rect x="562" y="4" width="74" height="72" rx="8" fill="#fff" stroke="#e8eaec"/>
  <circle cx="599" cy="40" r="10" fill="#3289d0" stroke="none"/>
</svg>

<h2 class="abs h2" style="left:0;top:1108px;width:1200px;text-align:center">Being a digital parent never been easier</h2>
<p class="abs" style="left:170px;top:1160px;width:860px;text-align:center;font-size:12.5px;line-height:26px;color:#444">We know that being an parent is not an easy task. Specially in this digital era. Kids constantly get to use various digital devices. And these devices comes with number of serious problems like viewing inappropriate content, cyberbullying and addiction. Limiting your Kids’ online time is not an solution for this. That’s why we took a step further to make sure your kid is safe out there.</p>
<a class="abs link" style="left:0;top:1261px;width:1200px;text-align:center">Learn more →</a>
<div class="abs" style="left:180px;top:1313px;width:839px;height:267px;border-radius:8px;background:radial-gradient(circle at 45% 40%,#4b4e52,#1a1c1f 70%)" role="img" aria-label="Video still of a child using a tablet in the dark"></div>
<svg class="abs" style="left:563px;top:1408px" width="72" height="72" viewBox="0 0 72 72"><circle cx="36" cy="36" r="34" fill="rgba(255,255,255,.2)" stroke="rgba(255,255,255,.7)" stroke-width="3"/><path d="M29 24l20 12-20 12z" fill="rgba(255,255,255,.8)"/></svg>

<!-- dashboard -->
<section class="abs band"></section>
<div class="abs app" style="left:205px;top:1713px;width:203px;height:397px;overflow:hidden">
  <div style="background:#5b9fd6;height:38px;color:#fff;font-size:10px;padding:4px 10px">
    <div style="font-size:7px">9:41 AM</div>
    <div style="display:flex;justify-content:space-between;margin-top:5px"><span>‹ Prev</span><span>Dashboard</span><span style="width:30px"></span></div>
  </div>
  <div style="padding:12px 20px">
    <div style="display:flex;align-items:center;gap:8px;font-size:8.5px"><i style="width:22px;height:22px;border-radius:50%;background:#c9a58e;display:block"></i>Kara's daily usage</div>
    <div style="display:flex;justify-content:space-between;align-items:center;margin:14px 0 8px"><b style="font-size:16px;font-weight:600">6h 56m</b><span style="font-size:8px">Monday, 26th 2020</span></div>
    <div class="app-row"><b style="background:#4a6fb0"></b><span>Friendloop</span></div>
    <div class="app-row"><b style="background:#d9568a"></b><span>Snapverse</span></div>
    <div class="app-row"><b style="background:#3fbf62"></b><span>Chatwell</span></div>
    <div class="app-row"><b style="background:#3aa2de"></b><span>Roamview</span></div>
  </div>
</div>
<div class="abs app" style="left:335px;top:1870px;width:204px;height:203px;padding:14px 20px">
  <b style="font-size:16px;font-weight:600;display:block;margin-bottom:6px">6h 56m</b>
  <div class="app-row"><b style="background:#4a6fb0"></b><span>Friendloop <small style="float:right;font-size:7px">2h 3m</small></span></div>
  <div class="app-row"><b style="background:#d9568a"></b><span>Snapverse <small style="float:right;font-size:7px">1h 5m</small></span></div>
  <div class="app-row"><b style="background:#3fbf62"></b><span>Chatwell <small style="float:right;font-size:7px">56m</small></span></div>
  <div class="app-row"><b style="background:#3aa2de"></b><span>Roamview <small style="float:right;font-size:7px">1h 56m</small></span></div>
</div>
<p class="abs eyebrow" style="left:600px;top:1836px;font-size:14px">Kelp Sentry Dashboard</p>
<h2 class="abs h2" style="left:600px;top:1860px">Track your childs’ website usage!</h2>
<p class="abs muted" style="left:600px;top:1904px;width:330px">Kelp Sentry parental control will constantly monitor your kids korvo usage and the new Dashboard shows what websites they have been visited.</p>

<!-- feature grid -->
<svg class="abs" style="left:126px;top:2244px" width="945" height="560" viewBox="0 0 945 560" stroke="#e6e8ea" stroke-width="1">
  <path d="M312 0V560M638 0V560M0 186H945M0 358H945"/>
</svg>
<svg width="0" height="0" style="position:absolute"><defs>
  <symbol id="ban" viewBox="0 0 24 24"><circle cx="12" cy="12" r="10" fill="none" stroke="#3289d0" stroke-width="2.4"/><path d="M5 5l14 14" stroke="#3289d0" stroke-width="2.4"/></symbol>
</defs></svg>
<div class="cell" style="left:126px;top:2294px"><svg width="24" height="24"><use href="#ban"/></svg><h4>Blocking Inappropriate Content</h4><p>We allow a parent to understand what their children are doing online and block inappropriate content.</p></div>
<div class="cell" style="left:443px;top:2294px"><svg width="24" height="24" viewBox="0 0 24 24" fill="none" stroke="#3289d0" stroke-width="2"><rect x="2" y="2" width="8" height="8"/><rect x="14" y="2" width="8" height="8"/><rect x="2" y="14" width="8" height="8"/><rect x="14" y="14" width="8" height="8"/></svg><h4>App Management</h4><p>Kelp Sentry will scan the device every hour and detect any risky apps that have been installed.</p></div>
<div class="cell" style="left:764px;top:2294px"><svg width="24" height="24" viewBox="0 0 24 24" fill="none" stroke="#3289d0" stroke-width="2.4"><path d="M12 2a10 10 0 1 1-9 6"/><path d="M12 7v5l3 2"/></svg><h4>Set Device Access Times</h4><p>You can set times that the device can access the Internet.</p></div>
<div class="cell" style="left:126px;top:2463px"><svg width="24" height="24"><use href="#ban"/></svg><h4>Track Website Usage</h4><p>We allow a parent to understand what their children are doing online and block inappropriate content.</p></div>
<div class="cell" style="left:443px;top:2463px"><svg width="24" height="24"><use href="#ban"/></svg><h4>Sample Feature 5</h4><p>Lorem ipsum dolor sit amet, consectetur adipiscing elit. Pellentesque sed lobortis nulla, eget ultrices magna.</p></div>
<div class="cell" style="left:764px;top:2463px"><svg width="24" height="24"><use href="#ban"/></svg><h4>Sample Feature 6</h4><p>Lorem ipsum dolor sit amet, consectetur adipiscing elit. Pellentesque sed lobortis nulla, eget ultrices magna.</p></div>
<div class="cell" style="left:126px;top:2632px"><svg width="24" height="24"><use href="#ban"/></svg><h4>Sample Feature 7</h4><p>Lorem ipsum dolor sit amet, consectetur adipiscing elit. Pellentesque sed lobortis nulla, eget ultrices magna.</p></div>
<div class="cell" style="left:443px;top:2632px"><svg width="24" height="24"><use href="#ban"/></svg><h4>Sample Feature 8</h4><p>Lorem ipsum dolor sit amet, consectetur adipiscing elit. Pellentesque sed lobortis nulla, eget ultrices magna.</p></div>
<div class="cell" style="left:764px;top:2632px"><svg width="24" height="24"><use href="#ban"/></svg><h4>Sample Feature 9</h4><p>Lorem ipsum dolor sit amet, consectetur adipiscing elit. Pellentesque sed lobortis nulla, eget ultrices magna.</p></div>

<!-- support -->
<div class="abs" style="left:0;top:2870px;width:682px;height:375px;background:radial-gradient(ellipse at 45% 70%,#5d6f86,#1d2838 65%)" role="img" aria-label="Photo of two children looking at a tablet under a blanket"></div>
<p class="abs eyebrow" style="left:776px;top:2953px">Customer Support</p>
<h2 class="abs h2" style="left:776px;top:2976px;font-size:27px;line-height:34px">Got questions?<br>We’re here for you.</h2>
<p class="abs" style="left:776px;top:3053px;width:300px;font-size:12.5px;line-height:21px;color:#444">Check out our FAQ or send us your messages and requests for better support</p>
<a class="abs link" style="left:776px;top:3117px">Contact us →</a>

<!-- reviews -->
<p class="abs eyebrow" style="left:0;top:3362px;width:1200px;text-align:center">Customer Reviews</p>
<h2 class="abs h2" style="left:0;top:3381px;width:1200px;text-align:center">What others are saying</h2>
<div class="abs card" style="left:200px"><p>Lorem ipsum dolor sit amet, consectetur adipiscing elit. Mauris in dictum diam. Mauris sem nisi, tristique vitae ornare sed, bibendum scelerisque lacus. Nam non varius dolor. Morbi lacinia leo in augue imperdiet tempus. Vestibulum quis mi dapibus, varius felis at.</p>
  <div class="author"><i role="img" aria-label="Reviewer portrait"></i><div><b>Nora L. Ashby</b><small>Lawyer</small></div></div></div>
<div class="abs card" style="left:469px"><p>Lorem ipsum dolor sit amet, consectetur adipiscing elit. Mauris in dictum diam. Mauris sem nisi, tristique vitae ornare sed, bibendum scelerisque lacus. Nam non varius dolor. Morbi lacinia leo in augue imperdiet tempus. Vestibulum quis mi dapibus, varius felis at.</p>
  <div class="author" style="left:52px"><i style="background:#7a4b3a" role="img" aria-label="Reviewer portrait"></i><div><b>Sylvia M. Brandt</b><small>Freelancer</small></div></div></div>
<div class="abs card" style="left:739px"><p>Lorem ipsum dolor sit amet, consectetur adipiscing elit. Mauris in dictum diam. Mauris sem nisi, tristique vitae ornare sed, bibendum scelerisque lacus. Nam non varius dolor. Morbi lacinia leo in augue imperdiet tempus.</p>
  <div class="author" style="left:52px"><i style="background:#a88776" role="img" aria-label="Reviewer portrait"></i><div><b>Karen D. Holt</b><small>Housewife</small></div></div></div>

<!-- footer -->
<svg class="abs" style="left:0;top:3890px" width="1200" height="130" viewBox="0 0 1200 130" fill="none" stroke="#3289d0" stroke-width="1">
  <path d="M0 61H246M258 67L282 92H330"/>
  <path d="M930 34L950 15H1200"/><circle cx="954" cy="10" r="5" fill="#fff"/>
  <path d="M930 92L950 115H1200"/><circle cx="955" cy="120" r="5" fill="#fff"/>
  <circle cx="252" cy="61" r="5" fill="#fff"/>
</svg>
<nav class="abs footer-links"><a>HOME</a><a>ABOUT</a><a>PRICING</a><a>CONTACT US</a><a>HELP</a><a>TERMS OF USE</a><a>PRIVACY POLICY</a></nav>
<p class="abs copy">© 2020 KelpSentry All Rights Reserved.</p>

</body>
</html>
```